Business card design needed

My business is in Matchmaking. My objective is to find the most compatible partner for my clients....basically I'm in the love and happiness industry bringing two people together for a lasting loving relationship.

I envision the design to be something with 2 people who are in love looking happy or even a silhouette.....I don't really know, I'm open to ideas.....maybe no picture at all, but I want it to be classy :-)

I do have a logo which I will upload. You can also go to my website to give you an idea on the colours and the design if that helps, however the website is not finished yet, it should be up by today or tomorrow. If the website has a heart with swirls on the upper left hand corner, that is the old website, please ignore that one. The one that will be up shortly has a picture frame on the home page with my logo that will be in the file I will upload on this page.

Target Market(s)

There are three categories: Over 45, Asian and Western and same sex, but would be able to afford to hire a matchmaker

Contact Information for Business Card

The Tide Lantern
Helping You Find The "One"
Mira Feltham
Matchmaker
0472 915 264
info@thetidelantern.com.au
www.thetidelantern.com.au

```html
<!DOCTYPE html>
<html lang="en">
<head>
<meta charset="utf-8">
<title>The Tide Lantern — Business Card</title>
<link href="https://fonts.googleapis.com/css2?family=Ledger&display=swap" rel="stylesheet">
<style>
  :root {
    --canvas: #ffffff;
    --slate: #687a79;
    --slate-light: #7a8e8c;
    --frame: #ffffff;
    --sage-text: #7f9594;
    --plum-text: #7b5c64;
    --figure-tone: #e3e7e7;
    --ink-light: #ffffff;
  }
  html, body {
    margin: 0;
    width: 1200px;
    height: 1000px;
    overflow: hidden;
    background: var(--canvas);
  }
  .card {
    position: absolute;
    left: 347px;
    top: 47px;
    width: 510px;
    height: 897px;
    box-sizing: border-box;
    border: 1px solid #1a1a1a;
    background: radial-gradient(ellipse 60% 45% at 50% 40%, var(--slate-light), var(--slate));
    overflow: hidden;
    font-family: "Ledger", serif;
  }
  .frame-art {
    position: absolute;
    left: 0;
    top: 0;
    width: 510px;
    height: 897px;
  }
  .brand {
    position: absolute;
    left: 0;
    right: 0;
    top: 150px;
    text-align: center;
    color: var(--ink-light);
  }
  .brand-dot {
    display: block;
    width: 56px;
    height: 56px;
    margin: 0 auto 18px;
    border-radius: 50%;
    background: var(--ink-light);
  }
  .brand-name {
    font-size: 34px;
    letter-spacing: 0.5px;
  }
  .tagline {
    position: absolute;
    left: 0;
    right: 0;
    top: 456px;
    text-align: center;
    font-size: 44px;
    line-height: 53px;
    font-weight: 400;
    margin: 0;
  }
  .tagline .line-one { color: var(--sage-text); display: block; }
  .tagline .line-two { color: var(--plum-text); display: block; }
  .contact {
    position: absolute;
    left: 0;
    right: 0;
    top: 750px;
    text-align: center;
    color: var(--ink-light);
    font-size: 21px;
    line-height: 24px;
  }
  .contact p { margin: 0; }
  .contact .phone { font-size: 22px; }
</style>
</head>
<body>
  <div class="card">
    <svg class="frame-art" viewBox="0 0 510 897" xmlns="http://www.w3.org/2000/svg">
      <path class="ogee-frame" fill="var(--frame)"
        d="M256,299 C223,321 183,327 153,333 C73,345 23,373 0,421 L0,601 C23,643 73,673 153,688 C193,695 233,703 256,723 C283,703 323,695 360,689 C443,675 493,643 510,605 L510,416 C483,368 443,345 360,333 C323,327 283,319 256,299 Z"/>
      <rect class="couple-figure" role="img" aria-label="Faint silhouette of an embracing couple"
        x="183" y="370" width="150" height="288" rx="40" fill="var(--figure-tone)"/>
    </svg>

    <div class="brand">
      <span class="brand-dot"></span>
      <div class="brand-name">The Tide Lantern</div>
    </div>

    <h1 class="tagline">
      <span class="line-one">Helping You</span>
      <span class="line-two">Find The “One”</span>
    </h1>

    <div class="contact">
      <p class="name">Mira Feltham Matchmaker</p>
      <p class="phone">0472 915 264</p>
      <p class="email">info@thetidelantern.com.au</p>
      <p class="web">www.thetidelantern.com.au</p>
    </div>
  </div>
</body>
</html>
```